Visitenkarten-Design für Integratives Business Coaching
Radoslava Tzvetkorina hat sehr zuverlässig, zügig und sorgfältig gearbeitet - herzlichen Dank!!
Zielgruppe
Ich bin Henrike Wendel | Beratung mit Weitblick | Gründungs- und Unternehmensberatung (ZEFO-HWK)
Integratives Business Coaching für Start Ups, Unternehmer und alle, die eine berufliche Veränderung planen und ihre Selbständigkeit erfolgreich meistern wollen!
Aufgabenstellung
Das Design der VISITENKARTE sollte dem bestehenden Design meiner aktuellen Website https://henrike-wendel.com angepasst sein, ELEGANT aussehen und SERIÖS wirken:
Schriftart: Open sans
Schriftfarben: #0b2161 blau | #a8140f rot
Farbverlauf im Logo + auf der Website:
#a8130f
#edae44
Slogan: Business & Bewusstsein
Logo mit Schriftzug: siehe Upload
Profilbild: siehe Upload (das Photo muss noch gezoomt + zugeschnitten werden)

```html
<!DOCTYPE html>
<html lang="de">
<head>
<meta charset="utf-8">
<title>Henrike Wendel – Visitenkarte</title>
<link rel="stylesheet" href="https://fonts.googleapis.com/css2?family=Open+Sans:wght@400;600&display=swap">
<style>
  :root {
    --backdrop: #e3e2e3;
    --card: #ffffff;
    --blue: #2b2163;
    --red: #c8342a;
    --accent: #e2531d;
    --grad-start: #b8180f;
    --grad-mid: #d9531b;
    --grad-end: #f0a11a;
    --text: #222222;
  }
  html, body {
    margin: 0;
    padding: 0;
    width: 1200px;
    height: 900px;
    overflow: hidden;
    background: var(--backdrop);
    font-family: "Open Sans", Arial, sans-serif;
  }
  .canvas { position: relative; width: 1200px; height: 900px; }
  .card {
    position: absolute;
    width: 540px;
    height: 310px;
    background: var(--card);
    box-shadow: 0 6px 18px rgba(0,0,0,0.18);
    overflow: hidden;
  }
  .card__band {
    position: absolute;
    left: 0; right: 0; bottom: 0;
    height: 14px;
    background: linear-gradient(90deg, var(--grad-start), var(--grad-mid) 45%, var(--grad-end));
  }
  .card--brand { left: 620px; top: 130px; }
  .card--contact { left: 40px; top: 460px; }

  .brand { display: flex; align-items: center; gap: 14px; }
  .brand__dot {
    flex: none;
    border-radius: 50%;
    background: var(--accent);
  }
  .brand__name { color: var(--blue); font-weight: 400; line-height: 1.1; white-space: nowrap; }
  .brand__tagline { color: var(--blue); margin-top: 4px; white-space: nowrap; }

  .card--brand .brand { position: absolute; left: 120px; top: 112px; }
  .card--brand .brand__dot { width: 64px; height: 64px; }
  .card--brand .brand__name { font-size: 36px; }
  .card--brand .brand__tagline { font-size: 15px; }

  .profile { position: absolute; left: 30px; top: 34px; width: 190px; text-align: center; }
  .profile__photo {
    display: block;
    width: 130px; height: 130px;
    margin: 0 auto 18px;
    border-radius: 50%;
    background: radial-gradient(circle at 50% 40%, #d9c6ad, #8a7560 70%, #3b3330);
  }
  .profile__name { color: var(--red); font-size: 24px; line-height: 1.1; white-space: nowrap; }
  .profile__tagline { color: var(--text); font-size: 10px; margin-top: 4px; }

  .card--contact .brand { position: absolute; left: 250px; top: 34px; gap: 10px; }
  .card--contact .brand__dot { width: 36px; height: 36px; }
  .card--contact .brand__name { font-size: 20px; }
  .card--contact .brand__tagline { font-size: 9px; }

  .contacts {
    position: absolute; left: 250px; top: 112px;
    list-style: none; margin: 0; padding: 0;
    color: var(--text); font-size: 13.5px; line-height: 1.3;
  }
  .contacts__item { display: flex; align-items: center; gap: 12px; margin-bottom: 16px; white-space: nowrap; }
  .contacts__icon {
    flex: none; width: 34px; height: 34px;
    border-radius: 9px;
    background: var(--accent);
    display: flex; align-items: center; justify-content: center;
  }
</style>
</head>
<body>
<main class="canvas">
  <section class="card card--brand">
    <div class="brand">
      <span class="brand__dot"></span>
      <div>
        <div class="brand__name">Henrike Wendel</div>
        <div class="brand__tagline">Beratung mit Weitblick</div>
      </div>
    </div>
    <div class="card__band"></div>
  </section>

  <section class="card card--contact">
    <div class="profile">
      <span class="profile__photo" role="img" aria-label="Porträtfoto von Henrike Wendel"></span>
      <div class="profile__name">Henrike Wendel</div>
      <div class="profile__tagline">Beratung mit Weitblick</div>
    </div>

    <div class="brand">
      <span class="brand__dot"></span>
      <div>
        <div class="brand__name">Henrike Wendel</div>
        <div class="brand__tagline">Beratung mit Weitblick</div>
      </div>
    </div>

    <ul class="contacts">
      <li class="contacts__item">
        <span class="contacts__icon">
          <svg width="18" height="18" viewBox="0 0 24 24" aria-hidden="true"><path d="M12 2a7 7 0 0 0-7 7c0 5 7 13 7 13s7-8 7-13a7 7 0 0 0-7-7z" fill="#fff"/><circle cx="12" cy="9" r="2.6" fill="#e2531d"/></svg>
        </span>
        <span>Kelterweg 7b<br>80997 München</span>
      </li>
      <li class="contacts__item">
        <span class="contacts__icon">
          <svg width="18" height="18" viewBox="0 0 24 24" aria-hidden="true"><path d="M6.6 10.8a15 15 0 0 0 6.6 6.6l2.2-2.2a1 1 0 0 1 1-.25 11.4 11.4 0 0 0 3.6.57 1 1 0 0 1 1 1V20a1 1 0 0 1-1 1A17 17 0 0 1 3 4a1 1 0 0 1 1-1h3.5a1 1 0 0 1 1 1c0 1.25.2 2.45.57 3.57a1 1 0 0 1-.25 1z" fill="#fff"/></svg>
        </span>
        <span>Tel: +49 89 41 27 63 08<br>Mobil: +49 151 304 72 916</span>
      </li>
      <li class="contacts__item">
        <span class="contacts__icon">
          <svg width="18" height="18" viewBox="0 0 24 24" aria-hidden="true"><rect x="3" y="6" width="18" height="12" rx="2" fill="#fff"/><path d="M4 7l8 6 8-6" stroke="#e2531d" stroke-width="1.6" fill="none"/></svg>
        </span>
        <span>willkommen@henrike-wendel.com<br>www.henrike-wendel.com</span>
      </li>
    </ul>
    <div class="card__band"></div>
  </section>
</main>
</body>
</html>
```